Prayer Service 12.28.2013

I need a flyer designed for a Christian prayer service. The title and theme is:
"Total and Complete Surrender for Total and Complete Deliverance!"
1. You have creative freedom with imagery and typography
2. I need a quick turnaround time
FLYER DETAILS:
A prayer, anointing, and deliverance all night prayer service, at Brightwater Assembly.
Saturday December 28 2013 from 9pm-6am.
Special guest speakers, prayer,anointing,and deliverance sessions.
For more information contact Sis Dorothy Whitfield at Brightwater Assembly 555 634 1297 Ext. 4816 or Monica Shaw at 555 802-3941

```html
<!DOCTYPE html>
<html lang="en">
<head>
<meta charset="utf-8">
<title>Total and Complete Surrender – All Night Prayer Service</title>
<link rel="stylesheet" href="https://fonts.googleapis.com/css2?family=Noto+Sans+Mono:wght@600;700;800&family=Didact+Gothic&display=swap">
<style>
  :root {
    --backdrop: #d9d9da;
    --sky-top: #1f6fb8;
    --sky-mid: #5d9bd3;
    --cloud-light: #f4f3f6;
    --cloud-shade: #c9c6d0;
    --cloud-pink: #ddd0dc;
    --title-orange: #d0542b;
    --date-navy: #273f8c;
    --body-grey: #4a4a52;
  }
  * { margin: 0; padding: 0; box-sizing: border-box; }
  html, body {
    width: 1200px;
    height: 965px;
    overflow: hidden;
    background: var(--backdrop);
  }
  .stage {
    width: 1200px;
    height: 965px;
    display: flex;
    align-items: center;
    justify-content: center;
  }
  .flyer {
    position: relative;
    width: 580px;
    height: 905px;
    overflow: hidden;
    box-shadow: 0 6px 24px rgba(0,0,0,0.18);
  }
  .flyer-photo {
    position: absolute;
    inset: 0;
    background:
      radial-gradient(ellipse 45% 30% at 78% 16%, #4a2a2c 0%, #6a3d4a 45%, rgba(106,61,74,0) 100%),
      radial-gradient(ellipse 80% 25% at 40% 30%, var(--cloud-light) 0%, rgba(244,243,246,0) 100%),
      linear-gradient(180deg, var(--sky-top) 0%, var(--sky-mid) 14%, var(--cloud-light) 28%, var(--cloud-shade) 45%, var(--cloud-pink) 60%, var(--cloud-light) 78%, var(--cloud-shade) 100%);
  }
  .flyer-content {
    position: absolute;
    left: 0;
    right: 0;
    top: 330px;
    padding: 0 28px;
    text-align: center;
  }
  .title {
    font-family: "Noto Sans Mono", monospace;
    color: var(--title-orange);
    text-transform: uppercase;
    line-height: 0.98;
    text-align: left;
  }
  .title-small {
    display: block;
    font-size: 37px;
    font-weight: 600;
    letter-spacing: 1px;
  }
  .title-large {
    display: block;
    font-size: 72px;
    font-weight: 800;
    letter-spacing: -1px;
  }
  .details {
    margin-top: 22px;
    font-family: "Didact Gothic", sans-serif;
    font-size: 17px;
    line-height: 1.3;
    color: var(--body-grey);
  }
  .date {
    margin-top: 30px;
    font-family: "Noto Sans Mono", monospace;
    color: var(--date-navy);
    font-weight: 800;
    line-height: 1.05;
  }
  .date-day { display: block; font-size: 40px; letter-spacing: -1px; }
  .date-line { display: block; font-size: 19px; font-weight: 700; }
  .contact {
    margin-top: 34px;
    font-family: "Didact Gothic", sans-serif;
    font-size: 15.5px;
    line-height: 1.35;
    color: var(--body-grey);
  }
</style>
</head>
<body>
  <main class="stage">
    <article class="flyer">
      <div class="flyer-photo" role="img" aria-label="Photograph: white clouds under a blue sky with a woman in prayer, head bowed and hands raised, in the upper right"></div>
      <div class="flyer-content">
        <h1 class="title">
          <span class="title-small">Total and Complete</span>
          <span class="title-large">Surrender</span>
          <span class="title-small">For Total and Complete</span>
          <span class="title-large">Deliverance!</span>
        </h1>
        <p class="details">A prayer, anointing, and deliverance all night prayer service, at Brightwater Assembly. Special guest speakers, prayer,anointing,and deliverance sessions.</p>
        <p class="date">
          <span class="date-day">SATURDAY</span>
          <span class="date-line">DECEMBER 28 2013</span>
          <span class="date-line">9PM-6AM</span>
        </p>
        <p class="contact">For more information contact:<br>Sis Dorothy Whitfield at Brightwater Assembly<br>555 634 1297 Ext. 4816 or Monica Shaw at 555 802-3941</p>
      </div>
    </article>
  </main>
</body>
</html>
```